high-impact, conversion-focused website redesign for the government sector

Objective: To design and develop a high-impact, conversion-focused digital platform that solidifies Harrowgate Lumen Advisors (HLA) as the leading communications and strategy firm for government, defense, and industrial clients. The site must project authority, innovation, and sophisticated precision. See the creative breif for more information

Target Market(s)

Government contractors

Industry/Entity Type

Government, defense, industrials

Coding

Coded - Design and coding required

Number of Pages Required

5+ page

Font styles to use
Other font styles liked:
• See the current website

Requirements
Must have
• See design brief
Nice to have
• See design brief
Should not have
• See design brief

```html
<!DOCTYPE html>
<html lang="en">
<head>
<meta charset="utf-8">
<title>Harrowgate Lumen Advisors — Defense &amp; Technology Advisory</title>
<link href="https://fonts.googleapis.com/css2?family=Orbitron:wght@500;700;800&family=Montserrat:ital,wght@0,400;0,500;0,600;0,700;1,400&display=swap" rel="stylesheet">
<style>
:root{
  --navy-900:#0a2142;
  --navy-800:#0d2a50;
  --navy-700:#123461;
  --navy-600:#1e3d62;
  --card-navy:#17375f;
  --blue:#2391f0;
  --blue-light:#4aa6f5;
  --ink:#0d2748;
  --body:#4a5568;
  --muted:#8a94a6;
  --paper:#ffffff;
  --mist:#f3f5f8;
  --line:#e2e6ec;
}
*{margin:0;padding:0;box-sizing:border-box}
html,body{width:1200px;height:4566px;overflow:hidden}
body{position:relative;font-family:'Montserrat',sans-serif;color:var(--body);background:var(--paper)}
section,header,footer{position:absolute;left:0;width:1200px}
a{white-space:nowrap}

/* nav */
.site-nav{top:0;height:67px;background:var(--navy-800);border-bottom:1px solid rgba(255,255,255,.08);z-index:5}
.nav-links{position:absolute;top:27px;display:flex;gap:28px;font-size:11px;font-weight:600;letter-spacing:1.6px;color:#fff;white-space:nowrap}
.nav-links.left{left:89px}
.nav-links.right{left:946px}
.brand{position:absolute;left:50%;top:14px;transform:translateX(-50%);display:flex;flex-direction:column;align-items:center;gap:5px}
.brand-mark{width:16px;height:16px;background:var(--blue)}
.brand-name{font-family:'Montserrat',sans-serif;font-size:10px;font-weight:600;color:#fff;letter-spacing:.4px;white-space:nowrap}
.btn-contact{position:absolute;left:1010px;top:20px;width:100px;height:28px;background:var(--blue);color:#fff;font-family:'Orbitron',sans-serif;font-size:10px;font-weight:700;letter-spacing:1.6px;display:flex;align-items:center;justify-content:center}

/* hero */
.hero{top:0;height:670px;background:linear-gradient(120deg,#0a2142 0%,#0f2d55 55%,#0b2445 100%);clip-path:polygon(0 0,100% 0,100% 571px,0 670px)}
.hero-art{position:absolute;left:640px;top:90px;width:560px;height:430px;background:radial-gradient(ellipse at 60% 40%,rgba(50,110,180,.35),rgba(10,33,66,0) 70%)}
.hero-tag{position:absolute;left:89px;top:207px;padding:6px 10px;border-left:2px solid var(--blue);font-family:'Orbitron',sans-serif;font-size:9px;font-weight:700;letter-spacing:2px;color:var(--blue);white-space:nowrap}
.hero h1{position:absolute;left:89px;top:250px;font-family:'Orbitron',sans-serif;font-weight:800;font-size:58px;line-height:62px;color:#fff;letter-spacing:1px;white-space:nowrap}
.hero-lead{position:absolute;left:89px;top:390px;width:540px;padding-left:22px;border-left:3px solid var(--blue);font-size:15px;line-height:24px;color:#d5deea}
.btn{position:absolute;height:44px;display:flex;align-items:center;justify-content:center;font-family:'Orbitron',sans-serif;font-size:11px;font-weight:700;letter-spacing:2px;color:#fff;white-space:nowrap}
.btn-primary{background:var(--blue)}
.btn-ghost{border:1.5px solid #fff}

/* about */
.about{top:670px;height:673px;background:var(--paper)}
.about h2{position:absolute;left:89px;top:82px;font-family:'Orbitron',sans-serif;font-weight:800;font-size:30px;line-height:34px;color:var(--ink);white-space:nowrap}
.about h2 em{font-style:normal;color:var(--blue)}
.about-copy{position:absolute;left:89px;top:243px;width:480px;font-size:14px;line-height:25px}
.features{position:absolute;left:89px;top:408px;display:flex;gap:22px}
.feature{width:146px;white-space:nowrap}
.feature svg{display:block;margin-bottom:6px}
.feature strong{display:block;font-family:'Orbitron',sans-serif;font-size:11px;font-weight:600;color:var(--ink)}
.feature span{font-size:9px;color:var(--muted)}
.learn-more{position:absolute;left:89px;top:494px;font-family:'Orbitron',sans-serif;font-size:11px;font-weight:700;letter-spacing:2px;color:var(--ink)}
.about-photo{position:absolute;left:626px;top:87px;width:484px;height:420px;background:radial-gradient(circle at 50% 45%,#0a3dbd 0%,#1e5fe0 30%,#4d8fe6 60%,#9cc4ef 100%);box-shadow:0 20px 40px rgba(13,39,72,.25)}
.photo-quote{position:absolute;left:656px;top:417px;width:427px;height:62px;background:#fff;display:flex;align-items:center;padding-left:22px;font-size:14px;font-style:italic;font-weight:500;color:var(--ink)}

/* results */
.results{top:1343px;height:692px;background:linear-gradient(135deg,#0d2a50 0%,#123461 100%)}
.results h2{position:absolute;left:0;width:1200px;top:80px;text-align:center;font-family:'Orbitron',sans-serif;font-weight:700;font-size:40px;letter-spacing:9px;color:#fff}
.results .kicker{position:absolute;left:0;width:1200px;top:137px;text-align:center;font-family:'Orbitron',sans-serif;font-size:11px;font-weight:700;letter-spacing:3.5px;color:var(--blue)}
.stat{position:absolute;top:204px;width:323px;height:162px;background:var(--card-navy);border:1px solid rgba(255,255,255,.08);text-align:center}
.stat b{display:block;margin-top:28px;font-family:'Orbitron',sans-serif;font-weight:800;font-size:46px;color:#fff}
.stat b::after{content:"";display:block;width:40px;height:2px;background:var(--blue);margin:10px auto 0}
.stat span{display:block;margin:12px auto 0;width:250px;font-size:11px;line-height:16px;color:#c7d2e0;letter-spacing:.3px}
.quotes{position:absolute;left:89px;top:433px;width:1021px;height:179px;border-top:1px solid rgba(255,255,255,.1);border-bottom:1px solid rgba(255,255,255,.1);background:rgba(255,255,255,.02);display:flex}
.quote{flex:1;padding:34px 30px 0 34px;border-left:1px solid rgba(255,255,255,.1)}
.quote:first-child{border-left:0}
.quote p{font-size:14px;font-style:italic;line-height:23px;color:#a9b6c8}
.quote cite{display:flex;align-items:center;gap:10px;margin-top:16px;font-style:normal;font-size:9px;font-weight:700;letter-spacing:1px;color:var(--blue);white-space:nowrap}
.quote cite i{width:24px;height:24px;border-radius:50%;background:#2c4a70;color:#c7d2e0;font-style:normal;font-size:8px;display:flex;align-items:center;justify-content:center}

/* services */
.services{top:2035px;height:627px;background:var(--mist)}
.services h2{position:absolute;left:89px;top:84px;font-family:'Orbitron',sans-serif;font-weight:700;font-size:30px;color:var(--ink);white-space:nowrap}
.services h2::after{content:"";display:block;width:80px;height:3px;background:var(--blue);margin-top:10px}
.btn-outline{position:absolute;left:927px;top:90px;width:183px;height:36px;border:1.5px solid var(--ink);display:flex;align-items:center;justify-content:center;font-family:'Orbitron',sans-serif;font-size:10px;font-weight:700;letter-spacing:2px;color:var(--ink)}
.service{position:absolute;width:240px;background:#fff;padding:30px 26px 0;box-shadow:0 2px 8px rgba(13,39,72,.04)}
.service svg{display:block;margin-bottom:8px}
.service h3{font-family:'Orbitron',sans-serif;font-weight:600;font-size:14px;line-height:22px;color:var(--ink)}
.service p{margin-top:10px;font-size:11px;line-height:19px;color:var(--muted)}

/* process */
.process{top:2662px;height:700px;background:var(--paper)}
.process h2{position:absolute;left:0;width:1200px;top:84px;text-align:center;font-family:'Orbitron',sans-serif;font-weight:700;font-size:30px;color:var(--ink)}
.process .kicker{position:absolute;left:0;width:1200px;top:132px;text-align:center;font-size:11px;letter-spacing:3px;color:var(--muted)}
.process-line{position:absolute;left:191px;top:280px;width:816px;height:1px;background:var(--line)}
.step{position:absolute;top:213px;width:180px;margin-left:-90px;text-align:center}
.step-num{position:relative;width:68px;height:68px;margin:0 auto;border:3px solid var(--ink);border-radius:50%;background:#fff;display:flex;align-items:center;justify-content:center;font-family:'Orbitron',sans-serif;font-size:20px;font-weight:700;color:var(--ink)}
.step-num::after{content:"";position:absolute;right:-2px;top:-2px;width:11px;height:11px;border-radius:50%;background:var(--blue);border:2px solid #fff}
.step-icon{width:34px;height:34px;margin:28px auto 0;border-radius:50%;background:var(--mist);display:flex;align-items:center;justify-content:center}
.step h4{margin-top:12px;font-family:'Orbitron',sans-serif;font-size:10px;font-weight:700;line-height:14px;letter-spacing:.8px;color:var(--ink)}
.step p{margin-top:10px;font-size:9.5px;line-height:16px;color:var(--muted)}
.btn-cta{position:absolute;left:505px;top:500px;width:190px;height:43px;background:var(--blue);color:#fff;display:flex;align-items:center;justify-content:center;font-family:'Orbitron',sans-serif;font-size:12px;font-weight:700;letter-spacing:2.4px}

/* edge */
.edge{top:3288px;height:700px;background:var(--mist);clip-path:polygon(0 62px,100% 0,100% 560px,0 594px)}
.edge h2{position:absolute;left:0;width:1200px;top:80px;text-align:center;font-family:'Orbitron',sans-serif;font-weight:700;font-size:30px;color:var(--ink)}
.edge h2::after{content:"";display:block;width:80px;height:3px;background:var(--blue);margin:14px auto 0}
.edge-lead{position:absolute;left:270px;width:660px;top:184px;text-align:center;font-size:14px;line-height:24px}
.pillar{position:absolute;top:285px;width:323px;height:229px;background:#fff;text-align:center}
.pillar-icon{width:68px;height:68px;margin:34px auto 0;border-radius:50%;background:var(--mist);display:flex;align-items:center;justify-content:center}
.pillar h3{margin-top:26px;font-family:'Orbitron',sans-serif;font-weight:700;font-size:16px;color:var(--ink);letter-spacing:1px}
.pillar p{margin:12px auto 0;width:250px;font-size:11px;line-height:18px;color:var(--body)}

/* ecosystem */
.ecosystem{top:3850px;height:369px;background:var(--navy-600);z-index:-1}
.ecosystem h2{position:absolute;left:0;width:1200px;top:160px;text-align:center;font-family:'Orbitron',sans-serif;font-weight:800;font-size:50px;letter-spacing:9px;color:rgba(255,255,255,.1)}
.ecosystem .kicker{position:absolute;left:0;width:1200px;top:228px;text-align:center;font-family:'Orbitron',sans-serif;font-size:12px;font-weight:700;letter-spacing:4px;color:var(--blue)}

/* footer */
.site-footer{top:4219px;height:347px;background:var(--navy-800)}
.foot-brand{position:absolute;left:117px;top:64px;display:flex;flex-direction:column;align-items:center;gap:8px;width:180px}
.foot-brand .brand-mark{width:22px;height:22px}
.foot-brand .brand-name{font-size:11px}
.foot-about{position:absolute;left:137px;top:172px;width:220px;font-size:11px;line-height:19px;color:#8ea0b8}
.foot-col{position:absolute;top:76px}
.foot-col h5{font-family:'Orbitron',sans-serif;font-size:11px;font-weight:700;letter-spacing:2.5px;color:#fff;margin-bottom:20px;white-space:nowrap}
.foot-col li{list-style:none;font-size:11px;line-height:30px;color:#8ea0b8;display:flex;align-items:center;gap:10px;white-space:nowrap}
.socials{display:flex;gap:12px}
.socials i{width:34px;height:34px;border-radius:50%;background:rgba(255,255,255,.08)}
.copyright-wrap{position:absolute;left:89px;width:1021px;top:300px;border-top:1px solid rgba(255,255,255,.07)}
.copyright{position:absolute;left:0;width:1200px;top:316px;text-align:center;font-size:9px;color:#5f7390}
</style>
</head>
<body>

<header class="site-nav">
  <nav class="nav-links left"><span>HOME</span><span>ADVISORY SERVICES</span><span>ABOUT US</span></nav>
  <div class="brand"><span class="brand-mark"></span><span class="brand-name">HARROWGATE LUMEN ADVISORS</span></div>
  <nav class="nav-links right"><span>BLOG</span></nav>
  <a class="btn-contact">CONTACT</a>
</header>

<section class="hero">
  <div class="hero-art" role="img" aria-label="Faint blueprint-style technical drawing of aircraft and defense hardware"></div>
  <div class="hero-tag">DEFENSE &amp; TECHNOLOGY ADVISORY</div>
  <h1>ACCELERATE<br>YOUR MISSION.</h1>
  <p class="hero-lead">Harrowgate Lumen Advisors exists for one reason: To connect the federal ecosystem with the technologies that matter most to America and her allies.</p>
  <a class="btn btn-primary" style="left:89px;top:489px;width:272px">START THE CONVERSATION</a>
  <a class="btn btn-ghost" style="left:400px;top:489px;width:275px">EXPLORE OUR SERVICES</a>
</section>

<section class="about">
  <h2>PRECISION<br>COMMUNICATIONS FOR<br>THE <em>MISSIONS THAT<br>MATTER</em></h2>
  <p class="about-copy">We combine deep military experience, DoD support capabilities, and government technology communications expertise with a relentless national security focus. We don't just understand the landscape; we help shape it for the innovators protecting our future.</p>
  <div class="features">
    <div class="feature">
      <svg width="18" height="20" viewBox="0 0 18 20"><path d="M9 1 2 4v5c0 5 3 8 7 10 4-2 7-5 7-10V4z" fill="none" stroke="#2391f0" stroke-width="2"/><path d="M9 4v12" stroke="#2391f0" stroke-width="2"/></svg>
      <strong>DEFENSE EXPERTISE</strong><span>Gov, Space &amp; Industrial</span>
    </div>
    <div class="feature">
      <svg width="18" height="20" viewBox="0 0 18 20"><circle cx="9" cy="7" r="5" fill="none" stroke="#2391f0" stroke-width="2"/><path d="M5 11 4 19l5-3 5 3-1-8" fill="none" stroke="#2391f0" stroke-width="2"/></svg>
      <strong>AWARD WINNING</strong><span>Strategic Communications</span>
    </div>
    <div class="feature">
      <svg width="20" height="20" viewBox="0 0 20 20"><circle cx="10" cy="10" r="8" fill="none" stroke="#2391f0" stroke-width="2"/><circle cx="10" cy="10" r="4" fill="none" stroke="#2391f0" stroke-width="2"/><circle cx="10" cy="10" r="1.5" fill="#2391f0"/></svg>
      <strong>MISSION DRIVEN</strong><span>Results Oriented</span>
    </div>
  </div>
  <a class="learn-more">LEARN MORE →</a>
  <div class="about-photo" role="img" aria-label="Close-up photograph of a jet engine fan in deep blue light"></div>
  <div class="photo-quote">"Connecting the ecosystem."</div>
</section>

<section class="results">
  <h2>PROVEN RESULTS</h2>
  <div class="kicker">THAT DRIVE REAL GROWTH</div>
  <div class="stat" style="left:89px"><b>+72%</b><span>INCREASE IN DATABASE CONTACTS</span></div>
  <div class="stat" style="left:438px"><b>100+</b><span>STRATEGIC INTRODUCTIONS (DOD &amp; A&amp;D)</span></div>
  <div class="stat" style="left:787px"><b>570%</b><span>STOCK VALUATION GROWTH</span></div>
  <div class="quotes">
    <div class="quote"><p>"HLA's strategic guidance was instrumental in navigating the complex defense sector."</p><cite><i>IA</i>IRONVALE ALLOYS</cite></div>
    <div class="quote"><p>"Their network is unmatched. They opened doors we didn't know existed."</p><cite><i>BF</i>BEACON FORGE</cite></div>
    <div class="quote"><p>"A true partner in mission success. Precision and execution at every step."</p><cite><i>MV</i>MERIDIAN VANCE GROUP</cite></div>
  </div>
</section>

<section class="services">
  <h2>OUR SERVICES</h2>
  <a class="btn-outline">VIEW ALL SERVICES</a>

  <div class="service" style="left:89px;top:179px;height:170px">
    <svg width="20" height="22" viewBox="0 0 20 22"><rect x="3" y="1" width="14" height="20" fill="none" stroke="#8a94a6" stroke-width="2"/><path d="M7 6h2M11 6h2M7 10h2M11 10h2M7 14h2M11 14h2" stroke="#8a94a6" stroke-width="2"/></svg>
    <h3>Corporate Comms</h3><p>Strategic internal and external messaging for defense entities.</p></div>
  <div class="service" style="left:349px;top:179px;height:170px">
    <svg width="24" height="20" viewBox="0 0 24 20"><path d="M2 8v5h4l10 5V3L6 8z" fill="#8a94a6"/><path d="M6 13l2 6" stroke="#8a94a6" stroke-width="2"/></svg>
    <h3>Public Relations</h3><p>Media relations and storytelling that builds authority.</p></div>
  <div class="service" style="left:610px;top:179px;height:170px">
    <svg width="24" height="22" viewBox="0 0 24 22"><path d="M12 1 2 6h20z" fill="#8a94a6"/><path d="M5 8v9M10 8v9M14 8v9M19 8v9" stroke="#8a94a6" stroke-width="2.5"/><rect x="2" y="18" width="20" height="3" fill="#8a94a6"/></svg>
    <h3>Gov Affairs</h3><p>Navigating legislative landscapes and regulatory environments.</p></div>
  <div class="service" style="left:870px;top:179px;height:170px">
    <svg width="24" height="22" viewBox="0 0 24 22"><path d="M12 1 23 21H1z" fill="#8a94a6"/><path d="M12 8v6M12 16v2" stroke="#fff" stroke-width="2"/></svg>
    <h3>Crisis Comms</h3><p>Rapid response and reputation management in critical times.</p></div>

  <div class="service" style="left:89px;top:370px;height:176px">
    <svg width="26" height="22" viewBox="0 0 26 22"><rect x="3" y="2" width="20" height="14" fill="none" stroke="#8a94a6" stroke-width="2"/><path d="M1 19h24" stroke="#8a94a6" stroke-width="2"/><path d="M10 7 8 9l2 2M16 7l2 2-2 2" fill="none" stroke="#8a94a6" stroke-width="1.5"/></svg>
    <h3>Digital Marketing</h3><p>Targeted campaigns to reach key decision makers.</p></div>
  <div class="service" style="left:349px;top:370px;height:176px">
    <svg width="30" height="20" viewBox="0 0 30 20"><path d="M2 4h5v10H2zM23 4h5v10h-5z" fill="#8a94a6"/><path d="M7 5l6-2 4 2 6 0v8l-5 4-5-3-6-1z" fill="none" stroke="#8a94a6" stroke-width="2"/></svg>
    <h3>Strategic<br>Connections</h3><p>Facilitating partnerships that accelerate mission goals.</p></div>
  <div class="service" style="left:610px;top:370px;height:176px">
    <svg width="24" height="20" viewBox="0 0 24 20"><path d="M2 1v18h21" fill="none" stroke="#8a94a6" stroke-width="2"/><path d="M5 14l5-6 4 4 7-8" fill="none" stroke="#8a94a6" stroke-width="2"/></svg>
    <h3>Investor Relations</h3><p>Communicating value to stakeholders and financial markets.</p></div>
  <div class="service" style="left:870px;top:370px;height:176px">
    <svg width="22" height="22" viewBox="0 0 22 22"><rect x="2" y="4" width="18" height="16" fill="none" stroke="#8a94a6" stroke-width="2"/><path d="M2 8h18M6 1v5M16 1v5" stroke="#8a94a6" stroke-width="2"/><path d="M7 14l3 3 5-6" fill="none" stroke="#8a94a6" stroke-width="2"/></svg>
    <h3>Event Management</h3><p>High-impact events that drive engagement and networking.</p></div>
</section>

<section class="process">
  <h2>WHAT TO EXPECT</h2>
  <div class="kicker">WHEN PARTNERING WITH US</div>
  <div class="process-line"></div>

  <div class="step" style="left:191px">
    <div class="step-num">1</div>
    <div class="step-icon"><svg width="14" height="14" viewBox="0 0 14 14"><circle cx="6" cy="6" r="4" fill="none" stroke="#0d2748" stroke-width="2"/><path d="M9 9l4 4" stroke="#0d2748" stroke-width="2"/></svg></div>
    <h4>DISCOVERY &amp;<br>ALIGNMENT</h4><p>We dig into your mission, objectives, audience, and challenges.</p></div>
  <div class="step" style="left:395px">
    <div class="step-num">2</div>
    <div class="step-icon"><svg width="12" height="14" viewBox="0 0 12 14"><path d="M6 1 1 3v4c0 3 2 5 5 6 3-1 5-3 5-6V3z" fill="#0d2748"/></svg></div>
    <h4>RISK &amp; GAP<br>ASSESSMENT</h4><p>We identify vulnerabilities, blind spots, and opportunities.</p></div>
  <div class="step" style="left:599px">
    <div class="step-num">3</div>
    <div class="step-icon"><svg width="14" height="14" viewBox="0 0 14 14"><path d="M2 12 12 2M2 2l4 4M8 8l4 4" stroke="#0d2748" stroke-width="2.5"/></svg></div>
    <h4>STRATEGY &amp;<br>MESSAGING</h4><p>We craft targeted communications, narratives, and positioning.</p></div>
  <div class="step" style="left:803px">
    <div class="step-num">4</div>
    <div class="step-icon"><svg width="16" height="14" viewBox="0 0 16 14"><circle cx="5" cy="5" r="3" fill="none" stroke="#0d2748" stroke-width="2"/><circle cx="12" cy="10" r="2.5" fill="none" stroke="#0d2748" stroke-width="2"/></svg></div>
    <h4>FULL-SERVICE<br>EXECUTION</h4><p>We execute across communications, advisory, outreach &amp; engagement.</p></div>
  <div class="step" style="left:1007px">
    <div class="step-num">5</div>
    <div class="step-icon"><svg width="14" height="14" viewBox="0 0 14 14"><circle cx="7" cy="7" r="6" fill="none" stroke="#0d2748" stroke-width="1.5"/><circle cx="7" cy="7" r="3" fill="none" stroke="#0d2748" stroke-width="1.5"/><circle cx="7" cy="7" r="1" fill="#0d2748"/></svg></div>
    <h4>PRECISION &amp;<br>SUPPORT</h4><p>Ongoing optimization, real-time communication, and partnership support.</p></div>

  <a class="btn-cta">GET IN TOUCH</a>
</section>

<section class="ecosystem">
  <h2>ECOSYSTEM</h2>
  <div class="kicker">CONNECTING INNOVATION TO MISSION</div>
</section>

<section class="edge">
  <h2>THE HARROWGATE EDGE</h2>
  <p class="edge-lead">We combine deep federal sector insight with precision communications, strategic connectivity, and a mission-first approach that drives real results.</p>
  <div class="pillar" style="left:89px">
    <div class="pillar-icon"><svg width="18" height="24" viewBox="0 0 18 24"><path d="M9 1a7 7 0 0 0-4 13v3h8v-3A7 7 0 0 0 9 1z" fill="#2391f0"/><rect x="5" y="19" width="8" height="3" fill="#2391f0"/></svg></div>
    <h3>INSIGHT</h3><p>Deep understanding of defense, federal, and industrial ecosystems.</p></div>
  <div class="pillar" style="left:438px">
    <div class="pillar-icon"><svg width="26" height="24" viewBox="0 0 26 24"><rect x="9" y="1" width="8" height="6" fill="none" stroke="#2391f0" stroke-width="2"/><rect x="1" y="16" width="8" height="6" fill="none" stroke="#2391f0" stroke-width="2"/><rect x="17" y="16" width="8" height="6" fill="none" stroke="#2391f0" stroke-width="2"/><path d="M13 7v5M5 16v-4h16v4" fill="none" stroke="#2391f0" stroke-width="2"/></svg></div>
    <h3>NETWORK</h3><p>Unmatched access to decision-makers and key stakeholders.</p></div>
  <div class="pillar" style="left:787px">
    <div class="pillar-icon"><svg width="24" height="24" viewBox="0 0 24 24"><path d="M22 2c-6 0-11 3-13 9l4 4c6-2 9-7 9-13z" fill="#2391f0"/><path d="M9 11H4l3-4h5M13 15v5l4-3v-5" fill="#2391f0"/><path d="M6 16l-4 6 6-4z" fill="#2391f0"/></svg></div>
    <h3>EXECUTION</h3><p>Precision delivery and measurable outcomes for mission success.</p></div>
</section>

<footer class="site-footer">
  <div class="foot-brand"><span class="brand-mark"></span><span class="brand-name">HARROWGATE LUMEN ADVISORS</span></div>
  <p class="foot-about">Connecting the federal ecosystem with the technologies that matter most.</p>
  <div class="foot-col" style="left:402px">
    <h5>QUICK LINKS</h5>
    <ul><li>Home</li><li>Advisory Services</li><li>About Us</li><li>Blog</li><li>Contact</li></ul>
  </div>
  <div class="foot-col" style="left:666px">
    <h5>CONTACT INFO</h5>
    <ul>
      <li><svg width="12" height="10" viewBox="0 0 12 10"><rect x="0" y="0" width="12" height="10" fill="#2391f0"/><path d="M0 0l6 5 6-5" fill="none" stroke="#0d2a50" stroke-width="1.3"/></svg>info@harrowgatelumen.com</li>
      <li><svg width="12" height="12" viewBox="0 0 12 12"><path d="M2 1h3l1 3-2 1c1 2 2 3 4 4l1-2 3 1v3c-6 0-10-4-10-10z" fill="#2391f0"/></svg>(555) 123-4567</li>
      <li><svg width="10" height="14" viewBox="0 0 10 14"><path d="M5 0a5 5 0 0 0-5 5c0 4 5 9 5 9s5-5 5-9a5 5 0 0 0-5-5z" fill="#2391f0"/><circle cx="5" cy="5" r="2" fill="#0d2a50"/></svg>Washington, DC</li>
    </ul>
  </div>
  <div class="foot-col" style="left:932px">
    <h5>FOLLOW US</h5>
    <div class="socials"><i></i><i></i><i></i></div>
  </div>
  <div class="copyright-wrap"></div>
  <div class="copyright">©2025 Harrowgate Lumen Advisors. All Rights Reserved.</div>
</footer>

</body>
</html>
```